Ridgeway Business Card Redesign

Using the current logo/tagline lock-up and icon, redesign the Ridgeway business card to better show the tagline and improve the layout to give the card a more timely design and a classic, sophisticated look. See attached Project Brief for more detail.

```html
<!DOCTYPE html>
<html lang="en">
<head>
<meta charset="utf-8">
<title>Ridgeway Capital – Business Card</title>
<link rel="stylesheet" href="https://fonts.googleapis.com/css2?family=Open+Sans:wght@400;600&display=swap">
<style>
  :root {
    --backdrop: #5c5f63;
    --card: #ffffff;
    --brand-blue: #1773c1;
    --ink: #333538;
    --white: #ffffff;
  }
  html, body {
    margin: 0;
    width: 1200px;
    height: 884px;
    overflow: hidden;
    background: var(--backdrop);
  }
  .card {
    position: absolute;
    left: 100px;
    top: 156px;
    width: 1000px;
    height: 572px;
    background: var(--card);
    overflow: hidden;
    font-family: "Open Sans", Arial, sans-serif;
    color: var(--ink);
  }
  .brand {
    position: absolute;
    left: 62px;
    top: 40px;
    display: flex;
    align-items: center;
    gap: 22px;
  }
  .brand-mark {
    width: 84px;
    height: 84px;
    border-radius: 50%;
    background: var(--brand-blue);
  }
  .brand-name {
    font-size: 46px;
    font-weight: 600;
    letter-spacing: 4px;
    color: var(--ink);
    line-height: 1;
  }
  .accent-band {
    position: absolute;
    left: 232px;
    right: 0;
    top: 140px;
    height: 32px;
    background: var(--brand-blue);
    color: var(--white);
    font-size: 17px;
    font-weight: 400;
    letter-spacing: 3px;
    text-transform: uppercase;
    line-height: 32px;
    padding-left: 16px;
  }
  .person {
    position: absolute;
    left: 90px;
    top: 232px;
  }
  .person-name {
    margin: 0;
    font-size: 31px;
    font-weight: 600;
    color: var(--brand-blue);
  }
  .person-title {
    margin: 4px 0 0;
    font-size: 23px;
    line-height: 1.35;
  }
  .contact {
    position: absolute;
    left: 560px;
    top: 268px;
    font-size: 24px;
    line-height: 1.4;
  }
  .address { margin: 0 0 8px; font-style: normal; }
  .contact-line {
    display: flex;
    align-items: center;
    gap: 10px;
    margin: 0;
  }
  .contact-line svg { width: 22px; height: 22px; fill: var(--brand-blue); flex: none; }
  .web-band {
    position: absolute;
    left: 0;
    bottom: 0;
    width: 470px;
    height: 64px;
    background: var(--brand-blue);
    clip-path: polygon(0 0, 438px 0, 470px 64px, 0 64px);
    color: var(--white);
    font-size: 25px;
    letter-spacing: 2px;
    line-height: 64px;
    padding-left: 52px;
    box-sizing: border-box;
  }
</style>
</head>
<body>
  <div class="card">
    <div class="brand">
      <span class="brand-mark"></span>
      <span class="brand-name">RIDGEWAY CAPITAL</span>
    </div>
    <div class="accent-band">Patient Partners in Growth</div>

    <div class="person">
      <p class="person-name">Daniel R. Whitmore</p>
      <p class="person-title">Principal &amp;<br>Chief Marketing Officer</p>
    </div>

    <div class="contact">
      <address class="address">41 Harbor View Lane<br>Suite 210<br>Milford, CT 06460</address>
      <p class="contact-line">
        <svg viewBox="0 0 24 24"><path d="M6.6 10.8a15.1 15.1 0 0 0 6.6 6.6l2.2-2.2c.3-.3.7-.4 1-.2 1.1.4 2.3.6 3.6.6.6 0 1 .4 1 1V20c0 .6-.4 1-1 1A17 17 0 0 1 3 4c0-.6.4-1 1-1h3.5c.6 0 1 .4 1 1 0 1.3.2 2.5.6 3.6.1.3 0 .7-.2 1z"/></svg>
        (555) 240-1870
      </p>
      <p class="contact-line">
        <svg viewBox="0 0 24 24"><path d="M6.6 10.8a15.1 15.1 0 0 0 6.6 6.6l2.2-2.2c.3-.3.7-.4 1-.2 1.1.4 2.3.6 3.6.6.6 0 1 .4 1 1V20c0 .6-.4 1-1 1A17 17 0 0 1 3 4c0-.6.4-1 1-1h3.5c.6 0 1 .4 1 1 0 1.3.2 2.5.6 3.6.1.3 0 .7-.2 1z"/></svg>
        (555) 240-1892 (Direct)
      </p>
      <p class="contact-line">
        <svg viewBox="0 0 24 24"><path d="M7 1h10a2 2 0 0 1 2 2v18a2 2 0 0 1-2 2H7a2 2 0 0 1-2-2V3a2 2 0 0 1 2-2zm0 3v14h10V4zm5 15.5a1 1 0 1 0 0 2 1 1 0 0 0 0-2z"/></svg>
        (555) 318-6624
      </p>
      <p class="contact-line">
        <svg viewBox="0 0 24 24"><path d="M2 5h20v14H2zm2 2v.4l8 5.3 8-5.3V7zm0 2.8V17h16V9.8l-8 5.3z"/></svg>
        dwhitmore@ridgewaycapital.com
      </p>
    </div>

    <div class="web-band">www.ridgewaycapital.com</div>
  </div>
</body>
</html>
```